Steelcrest Process Systems. Needs a Business Card Design

We need a business card design for an engineering company which supplies industrial components (pumps, compressors, mechanical seals) provides repairs and services for above mentioned equipments. We offer a uniqe engineering solutions which help our customers to increase the productivness of their manufacturings, and energy savings.

Target Market(s)

Chemical and energy plants, refineries. Food industry and private consumers in a less.

Industry/Entity Type

Business

Contact Information for Business Card

Stylish and sleek design oriented on industrial area.

Requirements
Should not have
• company name shortening

```html
<!DOCTYPE html>
<html lang="en">
<head>
<meta charset="utf-8">
<title>Steelcrest Process Systems — Business Card</title>
<link href="https://fonts.googleapis.com/css2?family=Open+Sans:wght@400;600;700&display=swap" rel="stylesheet">
<style>
  :root {
    --backdrop: #3a424c;
    --card: #ffffff;
    --brand-blue: #1e3a94;
    --accent-orange: #f5a11c;
    --text-grey: #8a8a8a;
    --card-shadow: rgba(0, 0, 0, 0.35);
  }
  * { margin: 0; padding: 0; box-sizing: border-box; }
  html, body {
    width: 1200px;
    height: 960px;
    overflow: hidden;
    background: var(--backdrop);
    font-family: "Open Sans", Arial, sans-serif;
  }
  .canvas {
    width: 1200px;
    height: 960px;
    display: flex;
    flex-direction: column;
    align-items: center;
    justify-content: center;
    gap: 44px;
  }
  .card {
    width: 700px;
    height: 400px;
    background: var(--card);
    border-radius: 28px;
    box-shadow: 0 10px 28px var(--card-shadow);
    display: flex;
    flex-direction: column;
    align-items: center;
    text-align: center;
    position: relative;
    overflow: hidden;
  }

  /* Front side */
  .card--front { justify-content: center; }
  .brand {
    display: flex;
    align-items: center;
    gap: 14px;
    color: var(--brand-blue);
    font-weight: 700;
    font-size: 34px;
    letter-spacing: 0.2px;
  }
  .brand__dot {
    width: 22px;
    height: 22px;
    border-radius: 50%;
    background: var(--brand-blue);
    flex: none;
  }
  .social-handle {
    margin-top: 56px;
    display: flex;
    align-items: center;
    gap: 8px;
    color: var(--text-grey);
    font-size: 15px;
  }
  .social-handle__dot {
    width: 11px;
    height: 11px;
    border-radius: 50%;
    background: var(--accent-orange);
  }

  /* Back side */
  .card--back { padding-top: 60px; }
  .card--back .brand { font-size: 30px; }
  .person { margin-top: 34px; }
  .person__name {
    color: var(--brand-blue);
    font-weight: 700;
    font-size: 24px;
    line-height: 1.1;
  }
  .person__role {
    color: var(--accent-orange);
    font-size: 18px;
    margin-top: 2px;
  }
  .contact-icons {
    margin-top: 20px;
    display: flex;
    gap: 8px;
  }
  .contact-icons svg { width: 32px; height: 32px; display: block; }
  .contact-list {
    margin-top: 14px;
    list-style: none;
    color: var(--text-grey);
    font-size: 19px;
    line-height: 1.35;
  }
</style>
</head>
<body>
<main class="canvas">

  <section class="card card--front" aria-label="Card front">
    <div class="brand">
      <span class="brand__dot"></span>
      <span class="brand__name">Steelcrest Process Systems</span>
    </div>
    <div class="social-handle">
      <span class="social-handle__dot"></span>
      <span>@SteelcrestPS</span>
    </div>
  </section>

  <section class="card card--back" aria-label="Card back">
    <div class="brand">
      <span class="brand__dot"></span>
      <span class="brand__name">Steelcrest Process Systems</span>
    </div>

    <div class="person">
      <p class="person__name">Daniel Marsh</p>
      <p class="person__role">President &amp; CEO</p>
    </div>

    <div class="contact-icons">
      <svg viewBox="0 0 32 32" aria-label="Phone">
        <circle cx="16" cy="16" r="16" fill="var(--brand-blue)"/>
        <path d="M11 9 l3 0 l1.5 4 l-2 1.5 a9 9 0 0 0 4 4 l1.5 -2 l4 1.5 l0 3 a2 2 0 0 1 -2 2 a13 13 0 0 1 -12 -12 a2 2 0 0 1 2 -2z" fill="#fff"/>
      </svg>
      <svg viewBox="0 0 32 32" aria-label="Fax">
        <circle cx="16" cy="16" r="16" fill="var(--brand-blue)"/>
        <rect x="11" y="8" width="10" height="5" fill="#fff"/>
        <rect x="8" y="13" width="16" height="8" rx="1.5" fill="#fff"/>
        <rect x="11" y="18" width="10" height="6" fill="#fff" stroke="var(--brand-blue)" stroke-width="1.2"/>
      </svg>
      <svg viewBox="0 0 32 32" aria-label="Email">
        <circle cx="16" cy="16" r="16" fill="var(--brand-blue)"/>
        <rect x="8" y="10.5" width="16" height="11" fill="none" stroke="#fff" stroke-width="1.6"/>
        <path d="M8 10.5 l8 6.5 l8 -6.5" fill="none" stroke="#fff" stroke-width="1.6"/>
      </svg>
      <svg viewBox="0 0 32 32" aria-label="Website">
        <circle cx="16" cy="16" r="16" fill="var(--brand-blue)"/>
        <g fill="none" stroke="#fff" stroke-width="1.4">
          <circle cx="16" cy="16" r="8"/>
          <ellipse cx="16" cy="16" rx="3.5" ry="8"/>
          <line x1="8" y1="16" x2="24" y2="16"/>
          <line x1="9.5" y1="12" x2="22.5" y2="12"/>
          <line x1="9.5" y1="20" x2="22.5" y2="20"/>
        </g>
      </svg>
    </div>

    <ul class="contact-list">
      <li>(555) 014.2290</li>
      <li>(555) 014.2290</li>
      <li>info@steelcrestprocess.com</li>
      <li>www.steelcrestprocess.com</li>
    </ul>
  </section>

</main>
</body>
</html>
```